Design flat ui ios 7 inspired app

Know how you fit in the family and how you relate as a family through a shared Tree.
· Keep track of your family as it expands
· Merge family trees or join a common family Tree
· Share family moments by uploading pictures and videos on your calendar
· Get notifications of all events, additions, and other changes to the family tree
· Know where everyone is by keeping in touch through real-time chats
· Share your Tree with friends on social media
· Search for long lost family members and friends
· A great way for your kids to know where they come from

Providing a mobile app that allows users to not only create their family trees but allow them to invite other family members to participate in the completion of the family tree. • User downloads and installs the mobile app, then they proceed to signing up • Signing up the user should provide the following information; profile picture, first name, last name, date of birth, gender, password, email address, country, current city, mobile number • The next step is verifying the mobile number by asking the user to enter the six digit number that was sent to them via sms • Once the mobile number is verified your next step is to enter your family, start with you parents, then spouse(s) or partner(s), then siblings and children if any. This step should be optional, meaning users can skip this step • The app should have a menu bar at the bottom(action bar) with fiver menu items namely, Home, Edit, Tree, Stats, Calendar. • After the user has been signed in their first experience is the home screen, with the profile picture displayed, along with the user’s first name, last name, and age(all the above should be static). Just below all this are three tabs for notifications, photos, and birthdays. • The notifications tab will list all notifications one after the other in text form, example; Pete updated his high school, Bruno added a new member, Ursula has a graduation party coming up, Dmitri updated his work experience, Greta updated her maiden name, Hannah updated her siblings, Ernie updated his children etc. • Photo’s tab will list all pictures uploaded sorted by latest pictures uploaded and tagged in. One should be able to scroll through the pictures and then when they click on one they can slide though them one after the next viewing them. One should be able to go back to the home screen by clicking the back button. There should be an option to add more photos and share the current ones. • The last tab should be birthdays, which simply lists all birthdays of people who have been entered into the tree from parents to spouses to siblings to children. The birthdays should be listed sorted by month then day, and you should be able to see how old the person is turning. • The next menu bar is the Edit menu which has three tabs namely personal details, family and advanced details. Personal details will have the profile picture, first name, second name, last name, date of birth, gender, twin(if twin then state), relationship status(list spouse if not single), city or place of birth, and living or not. The next tab is the family tab which list and allows you to edit parents, spouse, siblings, and children. The last tab is advanced details, which is hobbies, languages, education, and work experience. • Then the most important part of the app is the Tree function which displays the users family tree, this is all the people added so far and each person is represented by a square with smooth edges, first name and last name displayed first, then age with a green button showing online and a red one showing offline, and below a profile picture. All the relations showed by a line joining the related people. If the person has many spouses they should be stacked together and kids don’t have to show which parent us theirs. One should be able to edit a profile, view a profile, view stats, invite and share. When you invite that person an sms should be generated and the user can enter the mobile number of the family member and once the family members accepts the invitation they then are a member of the tree who can receive notifications on any changes on the tree. Anyone should be able to invite anyone and everyone should see all notifications from everyone who is a member. • The next menu is the statistics menu which displays gender stats, age distribution, birthdays, relationship status, zodiac signs, living vs not living • The last one is the calendar menu which has a calendar where people can add events, upload media, and when a day is clicked and has events on, they should show at the bottom one after the other.

```html
<!DOCTYPE html>
<html lang="en">
<head>
<meta charset="utf-8">
<title>Family Tree App Screens</title>
<link rel="stylesheet" href="https://fonts.googleapis.com/css2?family=Open+Sans:wght@300;400;600&display=swap">
<style>
  :root{
    --page:#ffffff;
    --screen-top:#ead3cf;
    --screen-mid:#dccaca;
    --screen-bottom:#c8c6cd;
    --ink:#2b2b30;
    --ink-soft:#5e5a60;
    --rule:rgba(255,255,255,.55);
    --tabbar-ink:#2f2f34;
    --accent:#7ddc3a;
    --hero-a:#e0686a;
    --hero-b:#6b4968;
    --tab-idle:#f1eef0;
    --today:#d8465f;
    --blue:#3fb8ee;
    --purple:#b85fe6;
    --red:#f0606a;
    --orange:#f59a3b;
    --cyan:#2fc4e8;
    --mint:#3fe094;
    --sky:#41a6f0;
  }
  *{box-sizing:border-box;margin:0;padding:0}
  html,body{width:1200px;height:675px;overflow:hidden;background:var(--page)}
  body{font-family:"Open Sans",Arial,sans-serif;color:var(--ink)}
  .stage{position:absolute;left:0;top:0;width:1366px;height:768px;transform:scale(.8785);transform-origin:0 0}
  .screen{position:absolute;overflow:hidden;background:linear-gradient(180deg,var(--screen-top) 0%,var(--screen-mid) 55%,var(--screen-bottom) 100%)}
  .screen--home{left:368px;top:153px;width:272px;height:464px}
  .screen--calendar{left:733px;top:153px;width:272px;height:464px}
  .screen--edit{left:566px;top:137px;width:272px;height:485px;box-shadow:0 0 18px rgba(0,0,0,.25);z-index:2}
  .abs{position:absolute}
  .photo{position:absolute;border-radius:50%;background:radial-gradient(circle at 50% 40%,#e8b49a 0%,#a8654a 55%,#5a3226 100%)}
  .tabbar{position:absolute;left:0;right:0;bottom:0;background:linear-gradient(180deg,#6d6b71,#58575d)}
  .tabbar .tab{position:absolute;width:50px;margin-left:-25px;text-align:center;font-size:6px;color:var(--tabbar-ink);top:7px}
  .tabbar .tab svg{display:block;margin:0 auto 3px;width:20px;height:20px}
  .tabbar .tab.is-active{color:var(--accent)}
  .profile-head{position:absolute;left:0;top:0;width:272px;height:61px}
  .profile-head .photo{left:20px;top:12px;width:42px;height:42px;border:2px solid #fff}
  .profile-name{position:absolute;left:77px;top:20px;font-size:18px;font-weight:400;color:#222}
  .menu-row{position:absolute;left:0;width:272px;height:53px;border-top:1px solid var(--rule)}
  .menu-row .icon{position:absolute;left:26px;top:13px;width:26px;height:26px;border-radius:50%;display:flex;align-items:center;justify-content:center}
  .menu-row .icon svg{width:14px;height:14px}
  .menu-title{position:absolute;left:66px;top:12px;font-size:11.5px;font-weight:400;color:#1e1e22}
  .menu-sub{position:absolute;left:66px;top:29px;font-size:6.5px;color:var(--ink-soft)}
  .chevron{position:absolute;left:252px;top:20px;width:8px;height:12px}
  .hero{position:absolute;left:0;top:0;width:272px;height:126px;background:linear-gradient(160deg,var(--hero-a) 0%,#b2545f 45%,var(--hero-b) 100%)}
  .hero .photo{left:91px;top:14px;width:78px;height:78px;border:2px solid rgba(255,255,255,.8)}
  .hero-name{position:absolute;left:0;width:260px;top:97px;text-align:center;font-size:13px;color:#fff}
  .home-tabs{position:absolute;left:0;top:126px;width:272px;height:35px}
  .home-tab{position:absolute;top:0;height:35px;width:86px;display:flex;align-items:center;justify-content:center}
  .home-tab--alerts{left:0;background:var(--accent)}
  .home-tab--photos{left:86px;background:var(--tab-idle)}
  .home-tab svg{width:15px;height:15px}
  .feed-row{position:absolute;left:0;width:272px;height:51px;border-bottom:1px solid var(--rule)}
  .feed-row .photo{left:10px;top:11px;width:28px;height:28px}
  .feed-name{position:absolute;left:52px;top:11px;font-size:9.5px;font-weight:600;color:#222}
  .feed-text{position:absolute;left:52px;top:26px;font-size:6.5px;color:var(--ink-soft)}
  .small{font-size:7px;color:#333}
  .temp{position:absolute;left:215px;top:24px;font-size:24px;font-weight:300;color:#333}
  .month{position:absolute;right:140px;top:70px;font-size:15px;font-weight:300;color:#333;white-space:nowrap}
  .month span{position:absolute;left:100%}
  .weekday,.day{position:absolute;width:30px;margin-left:-15px;text-align:center;color:#333}
  .weekday{font-size:7px;top:108px}
  .day{font-size:11px;line-height:22px;height:22px;z-index:0}
  .day.is-today{color:#fff}
  .day.is-today::before{content:"";position:absolute;left:4px;top:0;width:22px;height:22px;border-radius:50%;background:var(--today);z-index:-1}
  .day.is-marked::before{content:"";position:absolute;left:4px;top:0;width:21px;height:21px;border-radius:50%;border:1px solid #fff}
  .day.has-dot::after{content:"";position:absolute;left:14px;top:21px;width:3px;height:3px;border-radius:50%;background:#fff}
  .rule{position:absolute;left:0;width:272px;height:1px;background:var(--rule)}
  .event-title{position:absolute;right:100px;top:298px;font-size:11px;color:#333;white-space:nowrap}
  .event-bar{position:absolute;left:133px;top:375px;width:139px;height:42px;background:rgba(255,255,255,.45);border-left:2px solid #fff}
  .event-time{position:absolute;left:145px;top:390px;font-size:7px;color:#333}
  .event-text{position:absolute;left:172px;top:387px;font-size:10px;color:#222;white-space:nowrap}
</style>
</head>
<body>
<div class="stage">

  <section class="screen screen--home">
    <div class="hero">
      <div class="photo" role="img" aria-label="Profile photo of the user"></div>
      <div class="hero-name">Clara Whitfield</div>
    </div>
    <div class="home-tabs">
      <div class="home-tab home-tab--alerts">
        <svg viewBox="0 0 16 16"><path d="M8 1.5c-2.6 0-4.2 2-4.2 4.5v3.2L2.5 11.5h11L12.2 9.2V6c0-2.5-1.6-4.5-4.2-4.5z" fill="#fff"/><circle cx="8" cy="13.3" r="1.6" fill="#fff"/></svg>
      </div>
      <div class="home-tab home-tab--photos">
        <svg viewBox="0 0 16 16"><rect x="1.5" y="4" width="13" height="9.5" rx="1.5" fill="#b9b6ba"/><rect x="5.5" y="2.5" width="5" height="2.5" rx="1" fill="#b9b6ba"/><circle cx="8" cy="8.8" r="2.6" fill="var(--tab-idle)"/></svg>
      </div>
    </div>
    <div class="feed-row" style="top:161px"><div class="photo" role="img" aria-label="Portrait of Pete"></div><div class="feed-name">Pete</div><div class="feed-text">updated his high school</div></div>
    <div class="feed-row" style="top:212px"><div class="photo" role="img" aria-label="Portrait of Bruno"></div><div class="feed-name">Bruno</div><div class="feed-text">added a new member</div></div>
    <div class="feed-row" style="top:263px"><div class="photo" role="img" aria-label="Portrait of Ursula"></div><div class="feed-name">Ursula</div><div class="feed-text">has a graduation party coming up</div></div>
    <div class="feed-row" style="top:314px"><div class="photo" role="img" aria-label="Portrait of Dmitri"></div><div class="feed-name">Dmitri</div><div class="feed-text">updated his work experience</div></div>
    <div class="feed-row" style="top:365px;border-bottom:0"><div class="photo" role="img" aria-label="Portrait of Ernie"></div><div class="feed-name">Ernie</div><div class="feed-text">updated her maiden name</div></div>
    <nav class="tabbar" style="height:45px">
      <div class="tab is-active" style="left:25px"><svg viewBox="0 0 20 20"><path d="M10 2 1.5 10h2.5v8h4.5v-5h3v5H16v-8h2.5z" fill="var(--accent)"/></svg>Home</div>
      <div class="tab" style="left:76px"><svg viewBox="0 0 20 20"><path d="M4 14.5 13.5 5l2 2L6 16.5H4z" fill="var(--tabbar-ink)"/><rect x="3" y="17.5" width="14" height="1.5" fill="var(--tabbar-ink)"/></svg>Edit</div>
      <div class="tab" style="left:128px"><svg viewBox="0 0 20 20"><circle cx="10" cy="5" r="2.3" fill="var(--tabbar-ink)"/><path d="M4 3l6 5 6-5M10 8v11" stroke="var(--tabbar-ink)" stroke-width="2" fill="none"/></svg>Tree</div>
    </nav>
  </section>

  <section class="screen screen--calendar">
    <div class="abs small" style="left:136px;top:21px">AM</div>
    <svg class="abs" style="left:170px;top:18px" width="40" height="32" viewBox="0 0 40 32"><circle cx="26" cy="10" r="6" fill="none" stroke="#444" stroke-width="1.2"/><path d="M8 27h22a6 6 0 0 0 0-12 8 8 0 0 0-15-1 6 6 0 0 0-7 13z" fill="#fff" stroke="#444" stroke-width="1.2"/></svg>
    <div class="abs" style="left:217px;top:16px;font-size:5.5px;color:#333">NEW DELHI</div>
    <div class="temp">15°</div>
    <div class="month">November<span>&nbsp;•&nbsp;2014</span></div>
    <div class="weekday" style="left:144px">WED</div>
    <div class="weekday" style="left:179px">THU</div>
    <div class="weekday" style="left:214px">FRI</div>
    <div class="weekday" style="left:249px">SAT</div>
    <div class="day" style="left:144px;top:126px">30</div><div class="day" style="left:179px;top:126px">31</div><div class="day" style="left:214px;top:126px">1</div><div class="day" style="left:249px;top:126px">2</div>
    <div class="day has-dot" style="left:144px;top:152px">6</div><div class="day" style="left:179px;top:152px">7</div><div class="day" style="left:214px;top:152px">8</div><div class="day" style="left:249px;top:152px">9</div>
    <div class="day" style="left:144px;top:178px">13</div><div class="day" style="left:179px;top:178px">14</div><div class="day is-today" style="left:214px;top:178px">15</div><div class="day" style="left:249px;top:178px">16</div>
    <div class="day" style="left:144px;top:205px">20</div><div class="day" style="left:179px;top:205px">21</div><div class="day" style="left:214px;top:205px">22</div><div class="day" style="left:249px;top:205px">23</div>
    <div class="day" style="left:144px;top:231px">27</div><div class="day" style="left:179px;top:231px">28</div><div class="day is-marked" style="left:214px;top:231px">29</div><div class="day" style="left:249px;top:231px">30</div>
    <div class="rule" style="top:290px"></div>
    <div class="event-title">Lunch with Mirela</div>
    <div class="rule" style="top:331px"></div>
    <div class="event-bar"></div>
    <div class="event-time">12 PM</div>
    <div class="event-text">•&nbsp; Deliver wireframes</div>
    <nav class="tabbar" style="height:45px">
      <div class="tab" style="left:140px"><svg viewBox="0 0 20 20"><circle cx="10" cy="5" r="2.3" fill="var(--tabbar-ink)"/><path d="M4 3l6 5 6-5M10 8v11" stroke="var(--tabbar-ink)" stroke-width="2" fill="none"/></svg>Tree</div>
      <div class="tab is-active" style="left:192px"><svg viewBox="0 0 20 20"><rect x="2.5" y="4" width="15" height="14" rx="1.5" fill="none" stroke="var(--accent)" stroke-width="1.6"/><path d="M2.5 8h15M6 2v4M14 2v4" stroke="var(--accent)" stroke-width="1.6"/><path d="M5.5 11h2v2h-2zM9 11h2v2H9zM12.5 11h2v2h-2zM5.5 14h2v2h-2zM9 14h2v2H9z" fill="var(--accent)"/></svg>Calendar</div>
      <div class="tab" style="left:240px"><svg viewBox="0 0 20 20"><path d="M10 3a7 7 0 1 0 7 7h-7z" fill="var(--tabbar-ink)"/><path d="M11.5 1.5v7h7a7 7 0 0 0-7-7z" fill="var(--tabbar-ink)"/></svg>Stats</div>
    </nav>
  </section>

  <section class="screen screen--edit">
    <header class="profile-head">
      <div class="photo" role="img" aria-label="Profile photo of the user"></div>
      <div class="profile-name">Clara Whitfield</div>
    </header>

    <div class="menu-row" style="top:61px">
      <div class="icon" style="background:var(--blue)"><svg viewBox="0 0 14 14"><circle cx="7" cy="5" r="2.6" fill="none" stroke="#fff" stroke-width="1.2"/><path d="M2 13c0-3 2.2-4.6 5-4.6s5 1.6 5 4.6z" fill="none" stroke="#fff" stroke-width="1.2"/></svg></div>
      <div class="menu-title">User Setup</div><div class="menu-sub">Edit your user details photos and account settings</div>
      <svg class="chevron" viewBox="0 0 8 12"><path d="M1.5 1l5 5-5 5" stroke="#999" stroke-width="1.2" fill="none"/></svg>
    </div>
    <div class="menu-row" style="top:114px">
      <div class="icon" style="background:var(--purple)"><svg viewBox="0 0 14 14"><path d="M7 12.2 2 7.4A2.8 2.8 0 0 1 7 3.6a2.8 2.8 0 0 1 5 3.8z" fill="none" stroke="#fff" stroke-width="1.2"/></svg></div>
      <div class="menu-title">Health &amp; Wealth</div><div class="menu-sub">Hight, weight blood group &amp; others</div>
      <svg class="chevron" viewBox="0 0 8 12"><path d="M1.5 1l5 5-5 5" stroke="#999" stroke-width="1.2" fill="none"/></svg>
    </div>
    <div class="menu-row" style="top:167px">
      <div class="icon" style="background:var(--red)"><svg viewBox="0 0 14 14"><circle cx="5" cy="8" r="3.3" fill="none" stroke="#fff" stroke-width="1.2"/><circle cx="9" cy="8" r="3.3" fill="none" stroke="#fff" stroke-width="1.2"/></svg></div>
      <div class="menu-title">Martial Status</div><div class="menu-sub">Married with whom</div>
      <svg class="chevron" viewBox="0 0 8 12"><path d="M1.5 1l5 5-5 5" stroke="#999" stroke-width="1.2" fill="none"/></svg>
    </div>
    <div class="menu-row" style="top:220px">
      <div class="icon" style="background:var(--orange)"><svg viewBox="0 0 14 14"><rect x="2" y="4.5" width="10" height="7" rx="1" fill="none" stroke="#fff" stroke-width="1.2"/><path d="M5 4.5V3h4v1.5M2 7.5h10" stroke="#fff" stroke-width="1.2" fill="none"/></svg></div>
      <div class="menu-title">Work</div><div class="menu-sub">Where you are working now &amp; past</div>
      <svg class="chevron" viewBox="0 0 8 12"><path d="M1.5 1l5 5-5 5" stroke="#999" stroke-width="1.2" fill="none"/></svg>
    </div>
    <div class="menu-row" style="top:273px">
      <div class="icon" style="background:var(--cyan)"><svg viewBox="0 0 14 14"><path d="M1 5.5 7 3l6 2.5L7 8z" fill="#fff"/><path d="M3.5 7v3c1 1 6 1 7 0V7" stroke="#fff" stroke-width="1.2" fill="none"/></svg></div>
      <div class="menu-title">Education</div><div class="menu-sub">Where you did your school and college</div>
      <svg class="chevron" viewBox="0 0 8 12"><path d="M1.5 1l5 5-5 5" stroke="#999" stroke-width="1.2" fill="none"/></svg>
    </div>
    <div class="menu-row" style="top:326px">
      <div class="icon" style="background:var(--mint)"><svg viewBox="0 0 14 14"><path d="M7 13S2.8 8.6 2.8 5.6a4.2 4.2 0 0 1 8.4 0C11.2 8.6 7 13 7 13z" fill="none" stroke="#fff" stroke-width="1.2"/><circle cx="7" cy="5.6" r="1.5" fill="#fff"/></svg></div>
      <div class="menu-title">Places You've Lived</div><div class="menu-sub">where you lived and living</div>
      <svg class="chevron" viewBox="0 0 8 12"><path d="M1.5 1l5 5-5 5" stroke="#999" stroke-width="1.2" fill="none"/></svg>
    </div>
    <div class="menu-row" style="top:379px">
      <div class="icon" style="background:var(--sky)"><svg viewBox="0 0 14 14"><circle cx="3.5" cy="4" r="1.4" fill="#fff"/><circle cx="7" cy="4" r="1.4" fill="#fff"/><circle cx="10.5" cy="4" r="1.4" fill="#fff"/><path d="M2.2 12V6.5h2.6V12M5.7 12V6.5h2.6V12M9.2 12V6.5h2.6V12" stroke="#fff" stroke-width="1" fill="none"/></svg></div>
      <div class="menu-title">Family Members</div><div class="menu-sub">add ,edit your family members &amp; there details</div>
      <svg class="chevron" viewBox="0 0 8 12"><path d="M1.5 1l5 5-5 5" stroke="#999" stroke-width="1.2" fill="none"/></svg>
    </div>

    <nav class="tabbar" style="height:47px">
      <div class="tab" style="left:27px"><svg viewBox="0 0 20 20"><path d="M10 2 1.5 10h2.5v8h4.5v-5h3v5H16v-8h2.5z" fill="var(--tabbar-ink)"/></svg>Home</div>
      <div class="tab is-active" style="left:80px"><svg viewBox="0 0 20 20"><path d="M4 14.5 13.5 5l2 2L6 16.5H4z" fill="var(--accent)"/><rect x="3" y="17.5" width="14" height="1.5" fill="var(--accent)"/></svg>Edit</div>
      <div class="tab" style="left:134px"><svg viewBox="0 0 20 20"><circle cx="10" cy="5" r="2.3" fill="var(--tabbar-ink)"/><path d="M4 3l6 5 6-5M10 8v11" stroke="var(--tabbar-ink)" stroke-width="2" fill="none"/></svg>Tree</div>
      <div class="tab" style="left:188px"><svg viewBox="0 0 20 20"><rect x="2.5" y="4" width="15" height="14" rx="1.5" fill="none" stroke="var(--tabbar-ink)" stroke-width="1.6"/><path d="M2.5 8h15M6 2v4M14 2v4" stroke="var(--tabbar-ink)" stroke-width="1.6"/><path d="M5.5 11h2v2h-2zM9 11h2v2H9zM12.5 11h2v2h-2zM5.5 14h2v2h-2zM9 14h2v2H9z" fill="var(--tabbar-ink)"/></svg>Calendar</div>
      <div class="tab" style="left:239px"><svg viewBox="0 0 20 20"><path d="M10 3a7 7 0 1 0 7 7h-7z" fill="var(--tabbar-ink)"/><path d="M11.5 1.5v7h7a7 7 0 0 0-7-7z" fill="var(--tabbar-ink)"/></svg>Stats</div>
    </nav>
  </section>

</div>
</body>
</html>
```